Calloway needs a modernized design

We would like a modern update (that can be responsive) to our existing website. Attached are the two existing pages we would like new concepts of - our home page and a page about one of our locations.

Calloway is provides executive offices and virtual office services. Startups, law firms, and financial services are our primary clients. We would like a professional, clean design, leaning towards minimalist. We intend to greatly reduce/eliminate the long paragraphs of text.

Industry/Entity Type

Business Service

Number of Pages Required

2 page

Requirements
Must have
• A design that can be responsive
Nice to have
• Large image(s) on home page that rotate.

```html
<!DOCTYPE html>
<html lang="en">
<head>
<meta charset="utf-8">
<title>Calloway Business Centers</title>
<link href="https://fonts.googleapis.com/css2?family=Playfair+Display&family=Roboto+Condensed:ital,wght@0,400;0,500;0,700;1,700&family=Roboto:wght@400;500&display=swap" rel="stylesheet">
<style>
:root{
  --navy:#1d2b55;
  --navy-deep:#142044;
  --blue:#1e4f8e;
  --orange:#f26a1b;
  --teal:#38a9c9;
  --cyan:#3aa0c8;
  --ink:#1d2b55;
  --grey-text:#8a8f99;
  --light:#f1f1f1;
  --white:#ffffff;
}
*{margin:0;padding:0;box-sizing:border-box}
html,body{width:1200px;height:3358px;overflow:hidden}
body{position:relative;font-family:"Roboto Condensed",sans-serif;background:var(--white);color:var(--ink)}
.abs{position:absolute}
.topbar{left:0;top:0;width:1200px;height:30px;background:var(--navy);color:#fff;font-size:13px;display:flex;align-items:center;justify-content:space-between;padding:0 30px 0 54px}
.topbar .phone-ico{display:inline-block;width:16px;height:12px;background:#8b93a8;margin-right:8px;vertical-align:middle}
.social{display:flex;align-items:center;gap:4px}
.social span.dot{width:15px;height:15px;border-radius:50%;background:#fff;display:inline-block}
.header{left:0;top:30px;width:1200px;height:127px;background:#fff}
.brand{left:52px;top:62px;display:flex;align-items:center;gap:12px}
.brand .mark{width:60px;height:60px;border-radius:50%;background:var(--navy)}
.brand .name{font-family:"Playfair Display",serif;font-size:30px;color:var(--navy);letter-spacing:1px}
.nav{right:52px;top:30px;height:127px;display:flex;gap:39px;font-size:17px;font-weight:500;color:var(--navy);text-transform:uppercase}
.nav a{display:flex;align-items:center;color:inherit;text-decoration:none;position:relative}
.nav a.active{color:var(--orange)}
.nav a.active::before{content:"";position:absolute;left:-6px;right:-6px;top:0;height:4px;background:var(--orange)}
.hero{left:0;top:157px;width:1200px;height:515px;background:linear-gradient(90deg,#6d7072 0%,#b9bcbd 35%,#d9dbdb 60%,#c8cacb 100%)}
.hero-panel{left:0;top:157px}
.hero-kicker{left:768px;top:326px;font-size:14px;letter-spacing:6px;color:#7d8189;white-space:nowrap}
.hero-title{left:766px;top:344px;font-family:"Playfair Display",serif;font-size:56px;line-height:74px;color:var(--navy);white-space:nowrap}
.btn{display:flex;align-items:center;justify-content:center;color:#fff;font-family:"Playfair Display",serif;font-size:17px;text-transform:uppercase}
.btn-orange{background:var(--orange)}
.btn-teal{background:var(--teal)}
.services{left:0;top:672px;width:1200px;height:385px;background:var(--light)}
.card{background:#fff;box-shadow:0 2px 6px rgba(0,0,0,.18)}
.card.orange{background:var(--orange)}
.card .label{position:absolute;font-weight:700;font-style:italic;font-size:18px;line-height:21px;color:var(--navy);text-transform:uppercase;white-space:nowrap}
.card.orange .label{color:#fff}
.card .label b{color:var(--orange)}
.card.orange .label b{color:#fff}
.card .art{position:absolute}
.why{left:0;top:1057px;width:1200px;height:848px;background:linear-gradient(90deg,#1f3f77 0%,#1b2f62 55%,#152450 100%)}
.h-serif{font-family:"Playfair Display",serif;font-weight:400}
.why-title{left:49px;top:1146px;font-size:58px;line-height:68px;color:#fff;white-space:nowrap}
.sub{font-size:12px;line-height:17px;font-weight:700;text-transform:uppercase;letter-spacing:.4px}
.why-sub{left:49px;top:1303px;width:540px;color:var(--cyan)}
.section-h{font-size:43px;text-transform:uppercase}
.why-h{left:49px;top:1358px;color:#fff}
.copy{font-size:16px;line-height:21.3px;font-weight:500;text-align:justify}
.why-copy{color:#fff}
.community-h{left:611px;top:2110px;color:var(--orange)}
.low-title{left:611px;top:1972px;font-size:58px;color:var(--navy);white-space:nowrap}
.low-sub{left:611px;top:2055px;width:520px;color:var(--grey-text)}
.portfolio{left:0;top:2669px;width:1200px;height:649px;background:linear-gradient(180deg,#2d4478 0%,#243a6a 55%,#0f1c3a 100%)}
.port-title{left:0;top:2706px;width:1200px;text-align:center;font-size:58px;color:#fff}
.port-sub{left:340px;top:2783px;width:520px;text-align:center;color:#fff}
.footer{left:0;top:3072px;width:1200px;height:246px;background:rgba(15,26,52,.92)}
.fcol{top:3200px;color:#fff}
.fcol h4{font-family:"Roboto",sans-serif;font-weight:400;font-size:27px;margin-bottom:8px}
.fcol p{font-family:"Roboto",sans-serif;font-size:16px;line-height:19px;color:#e3e6ee}
.copyright{left:0;top:3318px;width:1200px;height:40px;background:var(--blue);color:#fff;font-family:"Roboto",sans-serif;font-size:15px;display:flex;align-items:center;justify-content:center}
</style>
</head>
<body>

<div class="abs topbar">
  <div><span class="phone-ico"></span>Dallas 214.555.0140 | Houston 713.555.0188</div>
  <div class="social">Follow Our Latest News On:&nbsp;<span class="dot"></span><span class="dot"></span><span class="dot"></span><span class="dot"></span><span class="dot"></span><span class="dot"></span><span class="dot"></span></div>
</div>

<div class="abs header"></div>
<div class="abs brand"><span class="mark"></span><span class="name">CALLOWAY</span></div>
<nav class="abs nav">
  <a class="active">Home</a><a>Properties</a><a>Virtual Tours &amp; Videos</a><a>Photos</a><a>Broker Referrals</a>
</nav>

<div class="abs hero" role="img" aria-label="Executive boardroom with leather chair and conference table"></div>
<svg class="abs hero-panel" width="1200" height="515" viewBox="0 0 1200 515"><polygon points="745,0 1200,0 1200,515 520,515" fill="#f4f5f5" fill-opacity="0.82"/></svg>
<div class="abs hero-kicker">WELCOME TO CALLOWAY</div>
<h1 class="abs hero-title h-serif">Executive Office<br>Solutions</h1>
<div class="abs btn btn-orange" style="left:768px;top:508px;width:178px;height:44px">Our Offers</div>

<div class="abs services"></div>
<div class="abs card" style="left:54px;top:716px;width:259px;height:260px">
  <div class="art" role="img" aria-label="Brown leather office chair" style="left:22px;top:30px;width:66px;height:215px;background:linear-gradient(#6b4a3a,#3b2a22);border-radius:10px"></div>
  <div class="label" style="left:100px;top:54px">Executive Office<br>Suites <b>&gt;&gt;</b></div>
</div>
<div class="abs card" style="left:327px;top:716px;width:264px;height:260px">
  <div class="art" role="img" aria-label="Red leather sofa" style="left:20px;top:40px;width:220px;height:110px;background:linear-gradient(#d92a1f,#9d140f);border-radius:12px"></div>
  <div class="label" style="left:68px;top:183px">On-Demand Meeting<br>Rooms <b>&gt;&gt;</b></div>
</div>
<div class="abs card orange" style="left:607px;top:716px;width:264px;height:121px">
  <div class="label" style="left:16px;top:18px">On-Demand Training<br>Rooms <b>&gt;&gt;</b></div>
  <div class="art" role="img" aria-label="Purple lounge sofa" style="left:110px;top:62px;width:140px;height:46px;background:linear-gradient(#c02a9a,#7d1465);border-radius:10px"></div>
</div>
<div class="abs card orange" style="left:607px;top:853px;width:264px;height:123px">
  <div class="art" role="img" aria-label="Round wooden side table" style="left:14px;top:10px;width:100px;height:105px;background:linear-gradient(#7a3a1c,#3d1b0c);border-radius:50% 50% 10px 10px"></div>
  <div class="label" style="left:124px;top:64px">Virtual Office<br>Solutions <b>&gt;&gt;</b></div>
</div>
<div class="abs card" style="left:884px;top:716px;width:262px;height:260px">
  <div class="label" style="left:26px;top:38px">Video Conference<br>Solutions <b>&gt;&gt;</b></div>
  <div class="art" role="img" aria-label="Black leather armchair" style="left:68px;top:110px;width:145px;height:140px;background:linear-gradient(#3a3a3a,#111);border-radius:10px"></div>
</div>

<section class="abs why"></section>
<h2 class="abs why-title h-serif">Come See Why Smarter Companies<br>are Choosing US!</h2>
<div class="abs sub why-sub">Calloway Business Centers' Dallas, Ft. Worth and Houston executive office suites, virtual offices, meeting rooms and video conferencing.</div>
<h3 class="abs section-h h-serif why-h">Our Value:</h3>
<p class="abs copy why-copy" style="left:54px;top:1424px;width:253px">Either you need Dallas/Ft. Worth Office Space, Dallas Executive Suites, Ft. Worth Executive Suites, Houston Office Space, Houston Executive Suites, or maybe you simply need a place to stop in and use an ondemand office or meeting room from time to time or utilize our local business phone numbers, phone answering or business addresses through one of our virtual office solutions. At Calloway, you will always find affordable and</p>
<p class="abs copy why-copy" style="left:327px;top:1424px;width:260px">beautiful, professional properties. To make decisions easy for our full service executive suite clients, we include everything in one upfront and honest price including the office, phone answering and 55 hours of conference room time per month (alone a value of over $1,600/mo). Our meeting room, training room, computer lab, conference room, board room and video conference room rentals are another tribute to that same philosophy of value.</p>
<div class="abs" role="img" aria-label="Modern conference room with wall of video screens" style="left:681px;top:1323px;width:519px;height:430px;background:linear-gradient(135deg,#3b4758 0%,#9aa4ad 45%,#e6e8ea 70%,#7c5a3e 100%)"></div>
<div class="abs btn btn-teal" style="left:54px;top:1782px;width:174px;height:43px">Our Offers</div>

<div class="abs" role="img" aria-label="Black leather sofa" style="left:0;top:1941px;width:549px;height:518px;background:linear-gradient(160deg,#4a4a4a 0%,#1c1c1c 60%,#0a0a0a 100%)"></div>
<h2 class="abs low-title h-serif">One Low Cost!</h2>
<div class="abs sub low-sub">Calloway Business Centers' Dallas, Ft. Worth and Houston executive office suites, virtual offices, meeting rooms and video conferencing.</div>
<h3 class="abs section-h h-serif community-h">Community:</h3>
<p class="abs copy" style="left:616px;top:2176px;width:248px">Either you need Dallas/Ft. Worth Office Space, Dallas Executive Suites, Ft. Worth Executive Suites, Houston Office Space, Houston Executive Suites, or maybe you simply need a place to stop in and use an ondemand office or meeting room from time to time or utilize our local business phone numbers, phone answering or business addresses through one of our virtual office solutions. At Calloway, you will always find affordable and</p>
<p class="abs copy" style="left:889px;top:2176px;width:260px">beautiful, professional properties. To make decisions easy for our full service executive suite clients, we include everything in one upfront and honest price including the office, phone answering and 55 hours of conference room time per month (alone a value of over $1,600/mo). Our meeting room, training room, computer lab, conference room, board room and video conference room rentals are another tribute to that same philosophy of value.</p>
<div class="abs btn btn-orange" style="left:616px;top:2534px;width:177px;height:43px">Our Offers</div>

<section class="abs portfolio" role="img" aria-label="Blurred office interior background"></section>
<h2 class="abs port-title h-serif">Our Portifolio</h2>
<div class="abs sub port-sub">Calloway Business Centers' Dallas, Ft. Worth and Houston executive office suites, virtual offices, meeting rooms and video conferencing.</div>
<div class="abs footer"></div>
<div class="abs" role="img" aria-label="Bright meeting room with glass wall, white table and wall screen" style="left:226px;top:2843px;width:748px;height:323px;background:linear-gradient(180deg,#e9ecee 0%,#cfd5d9 55%,#f7f8f8 100%)"></div>
<svg class="abs" style="left:172px;top:2984px" width="30" height="44" viewBox="0 0 30 44"><polyline points="24,4 8,22 24,40" fill="none" stroke="#fff" stroke-width="7"/></svg>
<svg class="abs" style="left:1006px;top:2984px" width="30" height="44" viewBox="0 0 30 44"><polyline points="6,4 22,22 6,40" fill="none" stroke="#fff" stroke-width="7"/></svg>

<div class="abs fcol" style="left:54px"><h4>About us</h4><p>Recent Projects<br>Careers<br>Find us</p></div>
<div class="abs fcol" style="left:251px"><h4>Services</h4><p>Recent Projects<br>Careers<br>Find us</p></div>
<div class="abs fcol" style="left:446px"><h4>Design</h4><p>Recent Projects<br>Careers<br>Find us</p></div>
<div class="abs fcol" style="left:627px"><h4>Development</h4><p>Recent Projects<br>Careers<br>Find us</p></div>
<div class="abs fcol" style="left:835px"><h4>Find Us</h4><p>Recent Projects<br>Careers<br>Register</p></div>
<div class="abs fcol" style="left:1032px"><h4>Contacts</h4><p>Recent Projects<br>Careers<br>Find us</p></div>

<div class="abs copyright">Copyright © 2016 Calloway. All rights reserved.</div>
</body>
</html>
```